Eye-catching Yellow Page Ad for Attorney's Office

We need a phone book advertisement for our law office. We practice workers' compensation law, and our clientele consists exclusively of individuals who have been injured on the job. The dimensions of the print ad will be 6" W X 4.54" H.

We've had our current ad for several years, and wanted to get a new one that has been designed by a professional. Being that it's an ad for a law firm, it needs to be professional looking, but we're hoping to have something that looks a little more modern and has eye-catching appeal. We like the text that is included in the ad, and we want to make sure our phone number is very visible. No real preference for color scheme.

I've attached a copy of our current ad. All the information included in there is accurate. Our office name is Thornbury & Lisle, PLLC. The ethical rules for attorney advertising require the PLLC to be included in the ad, but it can be smaller than the other text (see our current ad).

Target Market(s)

Our potential clients are injured workers looking for legal representation in their workers' compensation claim.

Industry/Entity Type

Attorney

Font styles to use
Serif
Sans Serif

Requirements
Must have
• Professional, but stands out from the crowd
Nice to have
• Clean modern design
Should not have
• We don't want it to be too crowded or over-worked.

```html
<!DOCTYPE html>
<html lang="en">
<head>
<meta charset="utf-8">
<title>Thornbury &amp; Lisle, PLLC — Workers' Compensation Ad</title>
<link rel="stylesheet" href="https://fonts.googleapis.com/css2?family=Questrial&display=swap">
<style>
  :root {
    --brand-blue: #1f74d6;
    --ink: #111111;
    --paper: #ffffff;
    --backdrop: #cfd7d8;
    --photo-warm: #8a5a2e;
    --photo-deep: #3a2414;
  }
  * { box-sizing: border-box; margin: 0; padding: 0; }
  html, body {
    width: 1200px; height: 1000px; overflow: hidden;
    background: var(--backdrop);
    font-family: "Questrial", "Century Gothic", sans-serif;
  }
  .ad {
    position: absolute; left: 188px; top: 150px;
    width: 825px; height: 700px;
    background: var(--brand-blue);
    color: var(--ink);
  }
  .ad__masthead {
    height: 84px;
    display: flex; align-items: center; justify-content: center;
    color: var(--paper);
    font-size: 62px; letter-spacing: 0.5px;
  }
  .ad__masthead .suffix { font-size: 32px; margin-left: 14px; align-self: flex-end; margin-bottom: 14px; }
  .ad__rule { height: 4px; background: var(--paper); margin: 0 0 3px; }
  .ad__body {
    position: relative;
    margin: 0 7px; height: 440px;
    background: var(--paper);
  }
  .ad__headline {
    text-align: center; font-size: 30px; line-height: 34px;
    padding-top: 8px;
  }
  .ad__headline .accent { color: var(--brand-blue); font-size: 28px; }
  .ad__photo {
    position: absolute; left: 22px; top: 100px;
    width: 338px; height: 322px;
    border: 4px solid var(--brand-blue);
    border-radius: 6px;
    transform: rotate(-3deg);
    background: linear-gradient(160deg, var(--photo-warm), var(--photo-deep));
    box-shadow: 2px 3px 6px rgba(0,0,0,.35);
  }
  .ad__pitch {
    position: absolute; left: 382px; top: 112px; width: 420px;
    font-size: 19px; line-height: 21px;
  }
  .ad__pitch .accent { color: var(--brand-blue); }
  .ad__lead { margin-top: 26px; font-size: 21px; }
  .services { list-style: none; margin: 18px 0 0 26px; }
  .services li {
    display: flex; align-items: center;
    color: var(--brand-blue); font-size: 19.5px; line-height: 23.5px;
  }
  .services svg { width: 16px; height: 16px; margin-right: 8px; flex: none; }
  .ad__rule--lower { height: 4px; background: var(--paper); margin-top: 6px; }
  .ad__contact {
    height: 93px; position: relative; color: var(--paper);
  }
  .ad__address {
    position: absolute; left: 22px; top: 30px;
    font-size: 30px; line-height: 30px;
  }
  .ad__phone {
    position: absolute; left: 385px; top: 4px;
    font-size: 62px; line-height: 62px;
  }
  .ad__web {
    position: absolute; left: 385px; top: 62px;
    font-size: 30px; line-height: 30px;
  }
  .ad__tagline {
    margin: 0 7px; height: 46px;
    background: var(--paper);
    display: flex; align-items: center; justify-content: center;
    font-size: 33px; letter-spacing: 0.5px; gap: 16px;
  }
  .ad__tagline .accent { color: var(--brand-blue); }
</style>
</head>
<body>
  <section class="ad">
    <header class="ad__masthead">Thornbury &amp; Lisle<span class="suffix">PLLC</span></header>
    <div class="ad__rule"></div>
    <div class="ad__body">
      <h1 class="ad__headline">Worker’s Compensation: <span class="accent">Former Assistant Attorneys<br>General Who Know The System</span></h1>
      <div class="ad__photo" role="img" aria-label="Photo of the two firm attorneys standing in a law library holding an open book"></div>
      <div class="ad__pitch">
        <p>At <span class="accent">Thornbury &amp; Lisle</span>, We provide Personal Attention to our Clients. That means your case is handled by an <span class="accent">Attorney</span> not an <span class="accent">Assistant.</span></p>
        <p class="ad__lead">We can help with:</p>
        <ul class="services">
          <li><svg viewBox="0 0 16 16"><path d="M1 9l4 5L15 2" fill="none" stroke="#111" stroke-width="3"/></svg>Workplace injuries or death</li>
          <li><svg viewBox="0 0 16 16"><path d="M1 9l4 5L15 2" fill="none" stroke="#111" stroke-width="3"/></svg>Lost wages</li>
          <li><svg viewBox="0 0 16 16"><path d="M1 9l4 5L15 2" fill="none" stroke="#111" stroke-width="3"/></svg>Medical Expenses &amp; Treatment</li>
          <li><svg viewBox="0 0 16 16"><path d="M1 9l4 5L15 2" fill="none" stroke="#111" stroke-width="3"/></svg>Hearing Loss Claims</li>
          <li><svg viewBox="0 0 16 16"><path d="M1 9l4 5L15 2" fill="none" stroke="#111" stroke-width="3"/></svg>Pension Claims</li>
          <li><svg viewBox="0 0 16 16"><path d="M1 9l4 5L15 2" fill="none" stroke="#111" stroke-width="3"/></svg>Disability Awards</li>
          <li><svg viewBox="0 0 16 16"><path d="M1 9l4 5L15 2" fill="none" stroke="#111" stroke-width="3"/></svg>Return to work issues</li>
        </ul>
      </div>
    </div>
    <div class="ad__rule--lower"></div>
    <div class="ad__contact">
      <p class="ad__address">427 N. Harbor<br>Suite 310, Bellingham.</p>
      <p class="ad__phone">360555-0142</p>
      <p class="ad__web">www.thornburylisle.com</p>
    </div>
    <p class="ad__tagline"><span>PROFESSIONAL</span><span>-</span><span class="accent">COMMITTED</span><span>-</span><span>EFFECTIVE</span></p>
  </section>
</body>
</html>
```